"Every Lantern Still Burning" Sermon Series Design

Needing a design for our church's next sermon series titled "Every Lantern Still Burning" where we will discuss the need for unity, diversity, love and clarity. Looking for a 1920 x 1080 (or higher res) editable and layered file (PSD or AI) so that we can reformat the design to work on social, screens, lower thirds and various print and online mediums. We will also need to have access to the font files so that we can make resize and tweak as needed. We like the idea of using a globe or map of the world as the backdrop with the words overtop. Or, the idea of creating a bunch of newspaper clippings (generic, so that they can't actually be read) and making the shape of a heart. See attached examples. This website will give you an idea of our previous sermon series designs so you can have an idea of our style (but, feel free to help us advance the ball on something more aligned with current design trends): https://www.brinmoorfellowship.church/series

Examples use red, but stay away from a ton of red. If you're gonna major in a color, use blue or something in that family.

Must haves:
Title: Every Lantern Still Burning
Tagline : (TBD - use some Lorem Ipsum as a placeholder and we will fill in later)
Our Logo (attached) (small towards bottom is standard - only use solid colors for logo - preferably just solid black or white)

Industry/Entity Type

Church

Font styles to use
Serif
Sans Serif

Requirements
Must have
• Title: Every Lantern Still Burning
Nice to have
• We like the idea of using a globe or map of the world as the backdrop with the words overtop. Or, the idea of creating a bunch of newspaper clippings (generic, so that they can't actually be read) and making the shape of a heart. See attached examples.

If you're gonna major on a color, stick with blue or something close.
Should not have
• Don't use red as the primary color (example we sent has red, but stay away from it)

```html
<!DOCTYPE html>
<html lang="en">
<head>
<meta charset="utf-8">
<title>Every Lantern Still Burning — Sermon Series</title>
<link href="https://fonts.googleapis.com/css2?family=Montserrat:wght@600;700&display=swap" rel="stylesheet">
<style>
  :root {
    --blue-deep: #0627d4;
    --blue-mid: #0752e0;
    --blue-light: #1c8ad6;
    --globe-edge: rgba(190, 215, 255, 0.55);
    --globe-core: rgba(120, 160, 245, 0.55);
    --white: #ffffff;
  }
  * { margin: 0; padding: 0; box-sizing: border-box; }
  html, body {
    width: 1200px;
    height: 675px;
    overflow: hidden;
    background: var(--blue-deep);
  }
  .series-slide {
    position: relative;
    width: 1200px;
    height: 675px;
    overflow: hidden;
    background: linear-gradient(170deg, var(--blue-deep) 0%, var(--blue-mid) 45%, var(--blue-light) 100%);
    font-family: "Montserrat", Arial, sans-serif;
    color: var(--white);
  }
  .light-streaks {
    position: absolute;
    inset: 0;
    width: 1200px;
    height: 675px;
  }
  .globe-backdrop {
    position: absolute;
    left: 244px;
    top: -27px;
    width: 730px;
    height: 730px;
    border-radius: 50%;
    background:
      radial-gradient(circle at 45% 40%, rgba(80, 120, 240, 0.35) 0%, rgba(80, 120, 240, 0) 60%),
      radial-gradient(circle at 50% 50%, var(--globe-core) 0%, rgba(150, 190, 250, 0.5) 75%, var(--globe-edge) 100%);
    box-shadow: 0 0 30px rgba(170, 205, 255, 0.35);
  }
  .series-title {
    position: absolute;
    left: 0;
    top: 62px;
    width: 1200px;
    text-align: center;
    font-weight: 700;
    font-size: 72px;
    line-height: 92px;
    letter-spacing: 0.36em;
    text-transform: uppercase;
  }
  .series-title span {
    display: block;
    padding-left: 0.36em;
  }
  .series-tagline {
    position: absolute;
    left: 0;
    top: 500px;
    width: 1200px;
    text-align: center;
    font-weight: 600;
    font-size: 23px;
    letter-spacing: 0.2em;
    padding-left: 0.2em;
  }
  .church-signature {
    position: absolute;
    left: 0;
    top: 572px;
    width: 1200px;
    display: flex;
    justify-content: center;
    align-items: center;
    gap: 10px;
  }
  .church-signature .mark-circle {
    width: 34px;
    height: 34px;
    border: 2.5px solid var(--white);
    border-radius: 50%;
  }
  .church-signature .church-name {
    font-weight: 600;
    font-size: 15px;
    letter-spacing: 0.18em;
    text-transform: uppercase;
  }
</style>
</head>
<body>
  <main class="series-slide">
    <svg class="light-streaks" viewBox="0 0 1200 675" aria-hidden="true">
      <polygon points="1200,0 1200,40 880,260 840,240" fill="rgba(255,255,255,0.05)"/>
      <polygon points="1200,310 1200,420 950,560 900,540" fill="rgba(255,255,255,0.04)"/>
      <polygon points="0,160 260,0 330,0 0,230" fill="rgba(255,255,255,0.03)"/>
    </svg>

    <div class="globe-backdrop" role="img" aria-label="Photograph of planet Earth seen from space, clouds over blue oceans, tinted blue"></div>

    <h1 class="series-title">
      <span>Every</span>
      <span>Lantern</span>
      <span>Still</span>
      <span>Burning</span>
    </h1>

    <p class="series-tagline">Lorem ipsum dolor sit amet</p>

    <div class="church-signature">
      <span class="mark-circle"></span>
      <span class="church-name">Brinmoor Fellowship</span>
    </div>
  </main>
</body>
</html>
```